POP/ROCK artist: CD Cover Design Project

IF U LOVE MUSIC AND ALBUM COVER ART THEN PLEASE PARTICIPATE IN MY PROJECT AND HAVE A GREAT TIME DESIGNING SOMETHING UNIQUE AND EXCITING!!!!
Hi, my name is tovo, a pop/rock artist living in Europe. i just finished recording a fun dance song, called FIZZY PAPER KITES, with a successful Quenmarsh Studios producer in Europe and I just put the finishing touches on the music video shot in LA. Now i'm going to release the song and video with Brivasong. It's going to go out to about 750 stores, including Plinkr, strumbly and all the other biggies as well as a load of smaller ones.
I need a great looking CD cover design that i can plaster everywhere . . . and i really mean everywhere i can.
As per Brivasong' specs, the cover art MUST BE 1500 x 1500 pixels. It cannot be blurry or pixilated and must be perfectly square.
I've uploaded some pics for you to choose from but you can use whichever one(s) you like . . . or none of them if you prefer, according to your inspiration. Just let me know if you want other pics and i can upload others.
Updates
Hey there,
Hey there,
Hi again, all,
Hey there,
Reason: Some designers are still revising their designs and we need more time.
Hi there, designers!
Hello everybody,
Target Market(s)
Modern pop/rock radio listeners of Tamblewick Radio, QFX, etc.
Please click on the following link to see the music video and hear the song:
http://www.vidcastro.example/watch?v=Qp7rTm2LwZa
Also, i have various pics and photos i can upload . . . just tell me what you need!!!!!
Requirements
Must have
- As per Brivasong' specs, the cover art MUST BE 1500 x 1500 pixels. It cannot be blurry or pixilated and must be perfectly square.
My artist name, tovo, and the song title, Fizzy Paper Kites, must be on the cover art.
The destination for your design is online music stores like Plinkr. So the dimensions will be VERY SMALL The actual size seen by the public will be about 1.5 cm x 1.5 cm! (Please have a look at the Plinkr store to see the actual size people will view the designs in.)
This means that your designs have to be clearly communicated at that size. The title of the song (fizzy paper kites) and my artist name (tovo) have to be large enough to read and whatever idea you're going for has to be easily understood.
Nice to have
- It should look totally modern and pop/rock, hip and cool. It's up to you and your design magic to do whatever you think it takes.
Should not have
- Website and e-mail addresses CANNOT be included anywhere on cover art.

```html
<!DOCTYPE html>
<html lang="en">
<head>
<meta charset="utf-8">
<title>tovo – Fizzy Paper Kites</title>
<link rel="stylesheet" href="https://fonts.googleapis.com/css2?family=Bowlby+One&family=Days+One&display=swap">
<style>
  :root {
    --signal-yellow: #fff200;
    --ink-black: #211e1c;
  }
  html, body {
    margin: 0;
    padding: 0;
    width: 1200px;
    height: 1200px;
    overflow: hidden;
    background: var(--signal-yellow);
  }
  .cover {
    display: block;
    width: 1200px;
    height: 1200px;
  }
  .ring--dark { fill: var(--ink-black); }
  .ring--light { fill: var(--signal-yellow); }
  .artist-name {
    font-family: "Bowlby One", "Arial Black", sans-serif;
    font-size: 92px;
    letter-spacing: 6px;
    fill: var(--ink-black);
    text-transform: uppercase;
  }
  .song-title {
    font-family: "Days One", "Arial Black", sans-serif;
    font-size: 82px;
    fill: var(--ink-black);
    text-transform: uppercase;
  }
</style>
</head>
<body>
<svg class="cover" viewBox="0 0 1200 1200" xmlns="http://www.w3.org/2000/svg" role="img" aria-label="tovo – Fizzy Paper Kites cover: concentric black and yellow rings">
  <defs>
    <path id="artist-arc" d="M 160 728 A 672 672 0 0 1 832 56" fill="none"/>
    <path id="title-arc" d="M 408 790 A 428 428 0 1 1 1260 728" fill="none"/>
  </defs>

  <g class="target-rings">
    <rect class="ring--light" x="0" y="0" width="1200" height="1200"/>
    <circle class="ring--dark" cx="832" cy="728" r="922"/>
    <circle class="ring--light" cx="832" cy="728" r="802"/>
    <circle class="ring--dark" cx="832" cy="728" r="650"/>
    <circle class="ring--light" cx="832" cy="728" r="545"/>
    <circle class="ring--dark" cx="832" cy="728" r="422"/>
    <circle class="ring--light" cx="832" cy="728" r="319"/>
    <circle class="ring--dark" cx="832" cy="728" r="212"/>
    <circle class="ring--light" cx="832" cy="728" r="128"/>
  </g>

  <text class="artist-name">
    <textPath href="#artist-arc" startOffset="395">tovo</textPath>
  </text>

  <text class="song-title">
    <textPath href="#title-arc" startOffset="8" textLength="960" lengthAdjust="spacing">Fizzy Paper Kites</textPath>
  </text>
</svg>
</body>
</html>
```